Langmore Plumbing Heating and Electric

We are looking for a basic, but very beautiful and professional looking website. We would like the ability for a customer to request service through our website via a form or email that will be forwarded to us. Other then that just contact info, our history, our rates, and the services we offer.

Look at his page, it is WAY TOO BASIC, but if gives a very general base line idea: http://www.dialfenwickpipes.example/

http://www.pipequarry.example/norfolk/?cmpid=10000&keyword=plumbing

http://www.valvewick-williamsburg.example/emergency_plumbing.html?keyphrase=emergency+plumbing+services

Target Market(s)

Heating, air conditioning, plumbing, natural gas

Industry/Entity Type

Plumbing

Number of Pages Required

4 page

Requirements
Must have
• Professional looking, very high end and modern,
Nice to have
• Would like the ability for client to contact us for service through the website utilizing some type of email.

```html
<!DOCTYPE html>
<html lang="en">
<head>
<meta charset="utf-8">
<title>Langmore Plumbing and Heating</title>
<link href="https://fonts.googleapis.com/css2?family=Lato:wght@400;700;900&display=swap" rel="stylesheet">
<style>
  :root {
    --brand-blue: #2ea6e0;
    --header-bg: rgba(22, 15, 11, 0.62);
    --hero-orange: rgba(200, 84, 10, 0.84);
    --panel-dark: #2f2f30;
    --footer-bg: #1e1e1e;
    --button-blue: #3a9be8;
    --text-light: #ffffff;
    --social-one: #1f78c8;
    --social-two: #2b9be6;
    --social-three: #cf3b2c;
  }
  * { margin: 0; padding: 0; box-sizing: border-box; }
  html, body { width: 1200px; height: 1000px; overflow: hidden; }
  body { font-family: "Lato", Arial, sans-serif; color: var(--text-light); background: var(--footer-bg); position: relative; }

  .hero {
    position: absolute; left: 0; top: 0; width: 1200px; height: 535px;
    background:
      radial-gradient(ellipse 300px 170px at 640px 110px, rgba(236,150,60,0.85) 0%, rgba(236,150,60,0) 100%),
      radial-gradient(ellipse 420px 220px at 880px 330px, rgba(214,120,70,0.45) 0%, rgba(214,120,70,0) 100%),
      linear-gradient(180deg, rgba(0,0,0,0) 60%, rgba(210,196,180,0.55) 88%, rgba(120,104,92,0.5) 100%),
      linear-gradient(90deg, #3b2619 0%, #5a3823 35%, #6e4a32 60%, #7a5640 100%);
  }
  .site-header {
    position: absolute; left: 0; top: 0; width: 1200px; height: 89px;
    background: var(--header-bg);
  }
  .brand {
    position: absolute; left: 252px; top: 24px;
    display: flex; align-items: center; gap: 10px;
    font-weight: 700; font-size: 36px; color: var(--brand-blue); line-height: 1;
  }
  .brand-dot { width: 12px; height: 12px; border-radius: 50%; background: var(--brand-blue); }
  .main-nav { position: absolute; top: 31px; left: 768px; display: flex; gap: 30px; font-family: Arial, Helvetica, sans-serif; font-size: 12px; }
  .main-nav a { color: var(--text-light); text-decoration: none; display: flex; align-items: center; gap: 6px; }
  .main-nav svg { width: 9px; height: 9px; }

  .services-card {
    position: absolute; left: 681px; top: 134px; width: 519px; height: 248px;
    background: var(--hero-orange); text-align: center;
  }
  .services-card h1 {
    font-weight: 700; font-size: 30px; margin-top: 15px; letter-spacing: -0.3px;
    text-shadow: 0 1px 3px rgba(0,0,0,0.35);
  }
  .services-list { list-style: none; margin-top: 6px; }
  .services-list li { font-size: 10.5px; font-weight: 700; text-transform: uppercase; line-height: 34.4px; }

  .repair-photo {
    position: absolute; left: 0; top: 535px; width: 730px; height: 383px;
    background:
      linear-gradient(180deg, rgba(255,255,255,0) 70%, rgba(40,50,80,0.15) 100%),
      linear-gradient(100deg, #5f80cf 0%, #7d9be0 30%, #c8b6a6 52%, #e9e6e2 70%, #f5f5f5 88%, #e2e0dc 100%);
  }
  .repair-panel {
    position: absolute; left: 730px; top: 535px; width: 470px; height: 383px;
    background: linear-gradient(180deg, #333334 0%, #2b2b2c 100%); text-align: center;
  }
  .repair-panel h2 { font-size: 26px; font-weight: 700; margin-top: 90px; }
  .repair-panel p { font-size: 10.4px; line-height: 15.4px; margin: 6px 20px 0 40px; font-weight: 700; }
  .repair-panel p strong { font-weight: 900; }
  .contact-button {
    position: absolute; left: 59px; top: 265px; width: 369px; height: 38px;
    background: var(--button-blue); color: var(--text-light); text-decoration: none;
    font-size: 11px; text-transform: uppercase; display: flex; align-items: center; justify-content: center;
  }

  .site-footer { position: absolute; left: 0; top: 918px; width: 1200px; height: 82px; background: var(--footer-bg); }
  .copyright {
    position: absolute; left: 250px; top: 16px; width: 350px; text-align: center;
    font-family: Arial, Helvetica, sans-serif; font-size: 11.5px; line-height: 15.5px;
  }
  .social-links { position: absolute; left: 711px; top: 15px; display: flex; gap: 8px; }
  .social-links a { display: flex; align-items: center; justify-content: center; width: 49px; height: 49px; border-radius: 2px; }
  .social-links a:nth-child(1) { background: var(--social-one); }
  .social-links a:nth-child(2) { background: var(--social-two); }
  .social-links a:nth-child(3) { background: var(--social-three); }
  .social-links svg { width: 24px; height: 24px; }
</style>
</head>
<body>
  <section class="hero" role="img" aria-label="Photo of a couple relaxing by a warm fireplace"></section>

  <header class="site-header">
    <div class="brand"><span class="brand-dot"></span>Langmore</div>
    <nav class="main-nav">
      <a href="#">Home</a>
      <a href="#">Services
        <svg viewBox="0 0 10 10"><path d="M1.5 3 L5 6.5 L8.5 3" fill="none" stroke="#fff" stroke-width="1.8"/></svg>
      </a>
      <a href="#">Contact</a>
    </nav>
  </header>

  <aside class="services-card">
    <h1>Gas and Heating Service's</h1>
    <ul class="services-list">
      <li>Gas Company Red Tags</li>
      <li>Thermostats</li>
      <li>Gas Furnaces</li>
      <li>Heat Pumps</li>
      <li>Dual Fuel Systems</li>
    </ul>
  </aside>

  <div class="repair-photo" role="img" aria-label="Photo of a technician working on gas piping"></div>
  <section class="repair-panel">
    <h2>Repair/Installation</h2>
    <p>We install gas lines for all your needs. Are you thinking of converting to natural gas, call us for a free quote to install your gas lines and appliances. We offer gas heating systems and water heaters for your home too. Gas appliances and piping should only be installed by qualified professionals, your comfort and safety could depend on it. Have a gas leak? Gas company <strong>red</strong> tagged your meter or furnace, we can find and repair that leak using modern leak detection methods.</p>
    <a class="contact-button" href="#">Contact Us</a>
  </section>

  <footer class="site-footer">
    <p class="copyright">Copyright © Langmore Plumbing, Heating, &amp; Electrical Inc. | All Rights Reserved</p>
    <div class="social-links">
      <a href="#" aria-label="Email us">
        <svg viewBox="0 0 24 24"><rect x="3" y="6" width="18" height="12" rx="1.5" fill="none" stroke="#fff" stroke-width="2"/><path d="M3.5 7 L12 13 L20.5 7" fill="none" stroke="#fff" stroke-width="2"/></svg>
      </a>
      <a href="#" aria-label="Call us">
        <svg viewBox="0 0 24 24"><path d="M6.5 3.5 L9.5 3.5 L11 8 L9 9.5 C10 12 12 14 14.5 15 L16 13 L20.5 14.5 L20.5 17.5 C20.5 19 19 20.5 17.5 20.5 C10 20 4 14 3.5 6.5 C3.5 5 5 3.5 6.5 3.5 Z" fill="#fff"/></svg>
      </a>
      <a href="#" aria-label="Find us">
        <svg viewBox="0 0 24 24"><path d="M12 2.5 C8 2.5 5 5.5 5 9.5 C5 14.5 12 21.5 12 21.5 C12 21.5 19 14.5 19 9.5 C19 5.5 16 2.5 12 2.5 Z" fill="#fff"/><circle cx="12" cy="9.5" r="2.8" fill="#cf3b2c"/></svg>
      </a>
    </div>
  </footer>
</body>
</html>
```